Consultancy Business Card Design

We need a business card design for a new company based in singapore called FortyOne. FortyOne a boutique consultancy firm offering broad-based business solutions, from conception to re-invention, for ventures from new start-ups to long-running traditional businesses.
Its 2 main divisions (Food & Beverage Operations and Construction & Project Management) have access to a wide range of networks, knowledge bases, and resources to service its clients across numerous diverse sectors. This includes, and is not limited to, construction, F&B, and retail.
We are a company that combines the ambition, boldness and energy of one in the 20s with the dedication, level-headedness and dependability of one entering its 30s. Bridging the experiences of the old with ideals of the young, we draw on the positives of both to create a unique synergy.
We hope to see designs that fits our company profile.
Boutique
FortyOne(Company Name)
Marcus Leow (Name)
Principle Consultant (Title)
F&B and Hospitality (Division)
(+65) 8364 5170 (Contact no.)
marcus@fortyone-example.com.sg (Email)

```html
<!DOCTYPE html>
<html lang="en">
<head>
<meta charset="utf-8">
<title>FortyOne Business Card</title>
<link rel="stylesheet" href="https://fonts.googleapis.com/css2?family=Aldrich&display=swap">
<style>
  :root {
    --page-bg: #e9e9e9;
    --card-black: #030303;
    --card-arc: #1b1b1b;
    --text-white: #f4f4f4;
    --title-yellow: #ecea1c;
    --division-green: #7dc143;
    --icon-blue: #63bfe8;
  }
  * { margin: 0; padding: 0; box-sizing: border-box; }
  html, body {
    width: 1200px;
    height: 1200px;
    overflow: hidden;
    background: var(--page-bg);
  }
  .canvas {
    width: 1200px;
    height: 1200px;
    display: flex;
    flex-direction: column;
    align-items: center;
    justify-content: center;
    gap: 64px;
    font-family: "Aldrich", sans-serif;
  }
  .card {
    position: relative;
    width: 880px;
    height: 503px;
    background: var(--card-black);
    overflow: hidden;
    box-shadow: 0 8px 24px rgba(0,0,0,0.25);
  }
  .company-name {
    position: absolute;
    color: var(--text-white);
    font-size: 50px;
    letter-spacing: 0.01em;
    line-height: 1;
    white-space: nowrap;
  }
  .card--front .company-name { left: 330px; top: 150px; }
  .card--back .company-name { right: 60px; top: 64px; }
  .back-arc {
    position: absolute;
    inset: 0;
    width: 100%;
    height: 100%;
  }
  .contact-block {
    position: absolute;
    left: 62px;
    top: 218px;
  }
  .person-name {
    color: var(--text-white);
    font-size: 38px;
    letter-spacing: 0.03em;
    margin-bottom: 10px;
  }
  .person-title {
    color: var(--title-yellow);
    font-size: 23px;
    margin-bottom: 8px;
  }
  .person-division {
    color: var(--division-green);
    font-size: 23px;
  }
  .divider {
    width: 410px;
    height: 2px;
    background: var(--text-white);
    margin: 12px 0 18px;
  }
  .contact-line {
    display: flex;
    align-items: center;
    gap: 12px;
    color: var(--text-white);
    font-size: 25px;
    letter-spacing: 0.04em;
    margin-bottom: 14px;
  }
  .contact-line svg { width: 28px; height: 22px; flex: none; }
</style>
</head>
<body>
<main class="canvas">
  <section class="card card--front" aria-label="Card front">
    <div class="company-name">FortyOne</div>
  </section>

  <section class="card card--back" aria-label="Card back">
    <svg class="back-arc" viewBox="0 0 880 503" aria-hidden="true">
      <path d="M0 118 C 300 118 610 260 700 503 L0 503 Z" fill="var(--card-arc)"/>
    </svg>
    <div class="company-name">FortyOne</div>
    <div class="contact-block">
      <p class="person-name">Marcus Leow</p>
      <p class="person-title">Principle Consultant</p>
      <p class="person-division">F&amp;B and Hospitality (Division)</p>
      <div class="divider"></div>
      <p class="contact-line">
        <svg viewBox="0 0 28 22" aria-hidden="true">
          <path d="M3 8 C3 3 25 3 25 8 L25 10 L19 10 L19 7 L9 7 L9 10 L3 10 Z" fill="var(--icon-blue)"/>
          <path d="M7 12 L21 12 L24 20 L4 20 Z" fill="var(--icon-blue)"/>
          <circle cx="14" cy="15.5" r="2.4" fill="var(--card-arc)"/>
        </svg>
        (+65) 8364 5170
      </p>
      <p class="contact-line">
        <svg viewBox="0 0 28 22" aria-hidden="true">
          <rect x="2" y="3" width="24" height="16" fill="var(--icon-blue)"/>
          <path d="M2 3 L14 12 L26 3" fill="none" stroke="var(--card-arc)" stroke-width="2"/>
        </svg>
        marcus@fortyone-example.com.sg
      </p>
    </div>
  </section>
</main>
</body>
</html>
```